Computer Support Rackcard

My company provides computer support services. Website is below:

www.nortekpcfix.com

The new service we are offering is Monthly Remote Support Service. I am trying to promote the service on a rackcard which I will give out to anyone who walks into my computer store. I want the design to be easy to read.

Our Remote Support service is available for $19.99 per pc and provides unlimited online computer support along with some extras such as antivirus and web filter to prevent computer viruses/malware. We would like to see designs that use royal blue color scheme and has a modern style like Vexel uses and is clean and easy to read.

I would like to somehow make the design look entertaining and would be interesting design wise. I hate templates so I want something that is not just a template with a picture and text added to it. Trying to be different with this design.
Updates

I uploaded a PSD file for my logo.

Target Market(s)

Target Customers are consumers with families with kids. Who are anywhere from age 40 to 65

Industry/Entity Type

Computer

Font styles to use
Serif
Sans Serif

Colors
0255a3
3176b5
85abd2
33a6d7
85cae6

Requirements
Must have
• Only 1 side of the rackcard needs to be designed.
Should not have
• The design should not have any pictures of people who appear to not be from United States. I don't want people to think my services are outsourced since they are not.

```html
<!DOCTYPE html>
<html lang="en">
<head>
<meta charset="utf-8">
<title>Remote Support Service Rack Card</title>
<link href="https://fonts.googleapis.com/css2?family=Bebas+Neue&family=Lato:wght@400;700;900&display=swap" rel="stylesheet">
<style>
  :root {
    --page-bg: #e6e7ea;
    --royal: #2a3593;
    --royal-deep: #1f2877;
    --royal-light: #3b4fb0;
    --photo-dark: #10263f;
    --photo-mid: #2a5a86;
    --photo-glow: #4f8fc4;
    --white: #ffffff;
    --ink: #1e1e1e;
    --tick: #1f2a7a;
    --rule-grey: #8a8f98;
    --seal-light: #ffffff;
    --seal-shade: #c9cbd0;
  }
  * { box-sizing: border-box; margin: 0; padding: 0; }
  html, body { width: 698px; height: 1200px; overflow: hidden; background: var(--page-bg); }
  .rack-card {
    position: absolute; left: 102px; top: 92px;
    width: 494px; height: 1016px;
    background: linear-gradient(160deg, var(--royal-light) 0%, var(--royal) 45%, var(--royal-deep) 100%);
    overflow: hidden;
    font-family: "Lato", sans-serif;
    color: var(--white);
    box-shadow: 0 4px 14px rgba(0,0,0,0.25);
  }
  .hero-photo {
    position: absolute; left: 0; top: 0; width: 494px; height: 340px;
    background:
      radial-gradient(circle at 30% 25%, var(--photo-glow) 0%, transparent 35%),
      linear-gradient(180deg, var(--photo-mid) 0%, var(--photo-dark) 100%);
  }
  .hero-wave { position: absolute; left: 0; top: 270px; width: 494px; height: 110px; }
  .headline {
    position: absolute; left: 0; right: 0; top: 384px;
    text-align: center;
    font-family: "Bebas Neue", sans-serif;
    font-size: 52px; letter-spacing: 0.5px; line-height: 1; font-weight: 400;
  }
  .intro {
    position: absolute; right: 30px; top: 455px; width: 440px;
    text-align: right; font-size: 23.5px; line-height: 32px;
  }
  .price-seal { position: absolute; left: 40px; top: 524px; width: 214px; height: 214px; }
  .price-seal svg { position: absolute; inset: 0; width: 100%; height: 100%; }
  .price-text {
    position: absolute; inset: 0;
    display: flex; flex-direction: column; align-items: center; justify-content: center;
    color: var(--ink); text-align: center;
  }
  .price-label { font-size: 21px; line-height: 26px; }
  .price-amount { font-size: 37px; font-weight: 900; line-height: 42px; }
  .price-unit { font-size: 37px; font-weight: 900; line-height: 42px; }
  .extras-box {
    position: absolute; left: 262px; top: 563px; width: 232px; height: 135px;
    background: var(--white); border-radius: 10px 0 0 10px;
    color: var(--ink); text-align: right;
    padding: 9px 8px 0 6px; font-size: 20.5px; line-height: 27.5px;
  }
  .extras-box .tick { display: inline-block; width: 14px; height: 12px; margin-right: 4px; }
  .service-tag {
    position: absolute; right: 30px; top: 715px;
    font-family: "Bebas Neue", sans-serif; font-size: 28px; line-height: 1;
  }
  .laptop-image {
    position: absolute; left: 252px; top: 762px; width: 210px; height: 160px;
    background: linear-gradient(135deg, #2f98c9 0%, #8fd0ec 40%, #d7dadf 72%, #9aa0a8 100%);
    border-radius: 6px;
  }
  .contact-heading {
    position: absolute; left: 32px; top: 802px;
    font-family: "Bebas Neue", sans-serif; font-size: 38px; line-height: 1; font-weight: 400;
  }
  .contact-line {
    position: absolute; left: 32px; display: flex; align-items: center; gap: 10px;
    font-size: 18.5px; line-height: 24px;
  }
  .contact-line svg { width: 15px; height: 15px; }
  .contact-phone { top: 866px; }
  .contact-email { top: 894px; }
  .footer-band { position: absolute; left: 0; top: 928px; width: 494px; height: 88px; }
  .web-address {
    position: absolute; left: 0; right: 0; top: 962px;
    text-align: center; color: var(--ink);
    font-size: 24px; letter-spacing: 3.5px;
  }
</style>
</head>
<body>
  <main class="rack-card">
    <div class="hero-photo" role="img" aria-label="Photo of a hand touching a glowing network of connected people icons"></div>
    <svg class="hero-wave" viewBox="0 0 494 110" preserveAspectRatio="none">
      <path d="M0 40 C 120 0, 260 10, 340 30 C 410 48, 460 40, 494 20 L494 110 L0 110 Z" fill="var(--white)"/>
      <path d="M0 70 C 110 30, 250 30, 340 48 C 410 62, 460 56, 494 44 L494 110 L0 110 Z" fill="var(--royal)"/>
    </svg>

    <h1 class="headline">Remote Support Service</h1>
    <p class="intro">We provide unlimited online<br>computer support along with some<br>extras</p>

    <div class="price-seal">
      <svg viewBox="0 0 200 200">
        <defs>
          <radialGradient id="sealFill" cx="40%" cy="35%" r="75%">
            <stop offset="0" stop-color="var(--seal-light)"/>
            <stop offset="0.6" stop-color="#eeeff1"/>
            <stop offset="1" stop-color="var(--seal-shade)"/>
          </radialGradient>
        </defs>
        <g fill="url(#sealFill)">
          <rect x="30" y="30" width="140" height="140" rx="22"/>
          <rect x="30" y="30" width="140" height="140" rx="22" transform="rotate(15 100 100)"/>
          <rect x="30" y="30" width="140" height="140" rx="22" transform="rotate(30 100 100)"/>
          <rect x="30" y="30" width="140" height="140" rx="22" transform="rotate(45 100 100)"/>
          <rect x="30" y="30" width="140" height="140" rx="22" transform="rotate(60 100 100)"/>
          <rect x="30" y="30" width="140" height="140" rx="22" transform="rotate(75 100 100)"/>
        </g>
      </svg>
      <div class="price-text">
        <span class="price-label">Available for</span>
        <span class="price-amount">$19.99</span>
        <span class="price-unit">PER PC</span>
      </div>
    </div>

    <div class="extras-box">
      <div><svg class="tick" viewBox="0 0 14 12"><path d="M1 6 L5 10 L13 1" stroke="var(--tick)" stroke-width="2.6" fill="none"/></svg>Antivirus</div>
      <div><svg class="tick" viewBox="0 0 14 12"><path d="M1 6 L5 10 L13 1" stroke="var(--tick)" stroke-width="2.6" fill="none"/></svg>Web filter to</div>
      <div>prevent computer</div>
      <div><svg class="tick" viewBox="0 0 14 12"><path d="M1 6 L5 10 L13 1" stroke="var(--tick)" stroke-width="2.6" fill="none"/></svg>Viruses/malware</div>
    </div>

    <p class="service-tag">Online Computer Support</p>
    <div class="laptop-image" role="img" aria-label="Open silver laptop with a blue wave screen"></div>

    <h2 class="contact-heading">Contact Us</h2>
    <p class="contact-line contact-phone">
      <svg viewBox="0 0 16 16"><rect x="0" y="0" width="16" height="16" rx="3" fill="var(--white)"/><path d="M5 3 L7 5.5 L6 7 C6.8 8.6 7.6 9.4 9 10 L10.5 9 L13 11 L11.5 13 C7 12.5 3.5 9 3 4.5 Z" fill="var(--royal)"/></svg>
      555-013-2468
    </p>
    <p class="contact-line contact-email">
      <svg viewBox="0 0 16 16"><rect x="0" y="3" width="16" height="11" fill="var(--white)"/><path d="M0.5 3.5 L8 9.5 L15.5 3.5" stroke="var(--royal)" stroke-width="1.4" fill="none"/></svg>
      help@nortekpcfix.com
    </p>

    <svg class="footer-band" viewBox="0 0 494 88" preserveAspectRatio="none">
      <path d="M0 10 C 150 22, 340 22, 494 8 L494 88 L0 88 Z" fill="var(--rule-grey)"/>
      <path d="M0 16 C 150 28, 340 28, 494 14 L494 88 L0 88 Z" fill="var(--white)"/>
    </svg>
    <p class="web-address">www.nortekpcfix.com</p>
  </main>
</body>
</html>
```